Protrait photographers business card

Need a new catchy, chic business card to promote my new portrait photograghy business. Love taking the natural, location portraits of families, children, teens. It should look classy, but also warm & friendly. I want it to show that Famliy, friends, couples & childten are what I love photographing, so if it can have that sort of feel to it & also looking energetic.

Target Market(s)

Families, couples, babies, people on holidays wanting some locational professional photos

Industry/Entity Type

Portrait Photography

Contact Information for Business Card

Lumivale photography, By Tavi, Norah Balfrey,Ph: 0487356024, Kestrel cove, Qld

Font styles to use
Decorative
Script

Requirements
Must have
• Company name & photographers name
Nice to have
• a coloured card
Should not have
• not be on a white card

```html
<!DOCTYPE html>
<html lang="en">
<head>
<meta charset="utf-8">
<title>Lumivale Photography – Business Card</title>
<link href="https://fonts.googleapis.com/css2?family=Pathway+Gothic+One&display=swap" rel="stylesheet">
<style>
  :root {
    --backdrop: #3a3a3a;
    --card: #231f20;
    --accent-red: #c8202f;
    --text-light: #f4f1ee;
  }
  html, body {
    margin: 0;
    padding: 0;
    width: 1200px;
    height: 842px;
    overflow: hidden;
    background: var(--backdrop);
  }
  .canvas {
    width: 1200px;
    height: 842px;
    display: flex;
    align-items: center;
    justify-content: center;
  }
  .business-card {
    position: relative;
    width: 900px;
    height: 514px;
    background: var(--card);
    box-sizing: border-box;
    font-family: "Pathway Gothic One", "Arial Narrow", sans-serif;
    color: var(--text-light);
    text-transform: uppercase;
  }
  .brand {
    position: absolute;
    left: 0;
    right: 0;
    top: 150px;
    text-align: center;
  }
  .brand-name {
    margin: 0;
    font-family: "Pathway Gothic One", "Arial Narrow", sans-serif;
    font-weight: 400;
    font-size: 150px;
    line-height: 1;
    letter-spacing: 6px;
    color: var(--accent-red);
    text-transform: none;
  }
  .brand-tagline {
    margin: 10px 0 0 0;
    padding-left: 300px;
    font-size: 30px;
    letter-spacing: 2px;
  }
  .contact-line {
    position: absolute;
    left: 0;
    right: 0;
    bottom: 48px;
    margin: 0;
    text-align: center;
    font-size: 27px;
    letter-spacing: 2px;
  }
</style>
</head>
<body>
<main class="canvas">
  <section class="business-card" aria-label="Lumivale Photography business card">
    <div class="brand">
      <h1 class="brand-name">Lumivale</h1>
      <p class="brand-tagline">Photography by Tavi</p>
    </div>
    <p class="contact-line">Norah Balfrey, Ph: 0487356024, Kestrel Cove, QLD</p>
  </section>
</main>
</body>
</html>
```